Range of 4 soft drink labels

The goal is to create a coherent sub-range, immediately identifiable as part of my beer universe, while assuming a lighter, more joyful and accessible personality.
common DNA of the 4 labels
Graphic style: modern, flat design enriched with light textures (grain, paper, micro-imperfections) to evoke the world of crafts.
Typography: a strong, legible, contemporary main typeface (sans-serif or grotesque), complemented by a more expressive or handwritten secondary typeface for the fun side.
Composition: clear structure, with a central axis or a block composition, similar to that of the beer range (same margins, same hierarchy logic).
Illustration: stylized, abstract or semi-figurative motifs (bubbles, plants, bursts, waves), avoiding realism to remain graphic and timeless.
Tone: joyful, refreshing, embracing pleasure without being childish.
Consistency: same label formats, same logic for name placement, same visual rhythm.
1. Cola – The iconic revisited
Color codes
Dominant deep red
Cream/ivory accents
Touches of black or dark brown for depth
Graphic intention
A cola that respects classic conventions but with a contemporary, artisanal touch. The red color is vibrant but slightly desaturated to avoid an industrial look.
Design
Textured red background, reminiscent of paper or ink.
Dynamic graphic patterns (curves, soft lightning bolts, stylized bubbles).
Robust, rounded typography with character.
A sensation of indulgence, roundness and energy.
Emotion
Confidence, pleasure, modernized nostalgia.
2. Tonic – Dry and elegant freshness
Color codes
Light blue, blue-grey or mineral blue
Off-white
Touches of silver or very light grey
Graphic intention
A clean, lively and elegant tonic, which evokes bitterness, freshness and finesse, without falling into cold luxury.
Design
A more airy composition than other soft drinks.
Patterns of fine bubbles, vertical lines or geometric shapes evoking tonicity.
Thinner or slightly condensed typography.
An immediate feeling of freshness.
Emotion
Freshness, precision, accessible sophistication.
3. Lemon-verbena lemonade – The refreshing botanical
Color codes
Pale yellow
Verbena green / sage green
Soft white
Graphic intention
Highlighting the natural and plant-based aspect, without falling into the organic cliché. A fresh, herbaceous, elegant drink.
Design
Stylized illustrations of verbena leaves and lemon peel.
Organic patterns, flowing lines.
Warm and contemporary typography.
A soft, luminous, slightly powdery palette.
Emotion
Nature, freshness, balance, craftsmanship.
4. Sparkling Lemonade – Sunshine and Energy
Color codes
Bright yellow dominant
Bright white
Touches of more acidic yellow or lime
Graphic intention
An ultra-fresh, cheerful and thirst-quenching lemonade that immediately catches the eye.
Design
Dynamic bubble patterns, bursts, circles.
A more rhythmic composition, almost in motion.
Expressive typography, slightly more playful.
Strong contrasts for an immediate visual impact.
Emotion
Sunshine, fun, a burst of freshness.
Consistency with the beer range (see www.tolvik.fr)
To ensure harmony with my existing range:
Same layout logic.
Same family of typefaces (dink / frail).
Same level of texture and detail.
Soft drinks appear as a lighter and more joyful version of the beer universe, not as a separate range.

```html
<!DOCTYPE html>
<html lang="en">
<head>
<meta charset="utf-8">
<title>Tolvik soft drink labels</title>
<link rel="stylesheet" href="https://fonts.googleapis.com/css2?family=Montserrat:wght@600;800&family=Kaushan+Script&display=swap">
<style>
  :root {
    --page: #f1f0ec;
    --ink: #2e3b45;
    --verbena-yellow: #f1e56c;
    --verbena-light: #f7ee9a;
    --sage: #7d9c83;
    --sage-dark: #5f7f69;
    --tonic-blue: #3fc3cf;
    --tonic-light: #7fd8e0;
    --cola-red: #a71d45;
    --cola-dark: #7d1433;
    --cream: #f6ead6;
    --lemon-white: #ffffff;
    --lime: #c8d41c;
    --lime-soft: #e6ec8c;
  }
  * { margin: 0; padding: 0; box-sizing: border-box; }
  html, body { width: 1200px; height: 1200px; overflow: hidden; }
  body { background: var(--page); position: relative; }
  .label-range {
    position: absolute; inset: 0;
    display: grid;
    grid-template-columns: 540px 540px;
    grid-template-rows: 284px 284px;
    gap: 80px 40px;
    justify-content: center;
    align-content: center;
  }
  .label { width: 540px; height: 284px; display: block; filter: drop-shadow(0 3px 6px rgba(0,0,0,.18)); }
  .brand-name { font-family: "Montserrat", sans-serif; font-weight: 800; font-size: 22px; letter-spacing: 1px; }
  .drink-name { font-family: "Montserrat", sans-serif; font-weight: 800; }
  .drink-type { font-family: "Kaushan Script", cursive; font-size: 30px; }
</style>
</head>
<body>
<svg width="0" height="0" style="position:absolute">
  <defs>
    <path id="label-shape" d="M0 85 H230 C250 85 262 70 272 52 A200 200 0 0 1 488 52 C498 70 510 85 530 85 H760 V315 H530 C510 315 498 330 488 348 A200 200 0 0 1 272 348 C262 330 250 315 230 315 H0 Z"/>
  </defs>
</svg>

<main class="label-range">

  <!-- Sparkling lemonade -->
  <svg class="label label--sparkling" viewBox="0 0 760 400">
    <defs>
      <linearGradient id="sparkling-bg" x1="0" y1="0" x2="1" y2="1">
        <stop offset="0" stop-color="#fbfcea"/>
        <stop offset="1" stop-color="#ffffff"/>
      </linearGradient>
    </defs>
    <use href="#label-shape" fill="url(#sparkling-bg)"/>
    <circle cx="326" cy="61" r="7" fill="var(--lime)"/>
    <text class="brand-name" x="390" y="69" text-anchor="middle" fill="var(--ink)">TOLVIK</text>
    <g role="img" aria-label="Lemon splash with rising bubbles illustration">
      <ellipse cx="380" cy="160" rx="55" ry="62" fill="var(--lime-soft)" opacity=".8"/>
    </g>
    <circle cx="300" cy="170" r="6" fill="none" stroke="var(--lime)" stroke-width="2"/>
    <circle cx="460" cy="140" r="9" fill="var(--lime)"/>
    <circle cx="440" cy="205" r="5" fill="var(--lime)"/>
    <text class="drink-name" x="380" y="268" text-anchor="middle" font-size="40" fill="var(--lime)" stroke="#3c3f18" stroke-width="1.5">sparkling</text>
    <text class="drink-name" x="380" y="306" text-anchor="middle" font-size="40" fill="var(--lime)" stroke="#3c3f18" stroke-width="1.5">lemonade</text>
    <text class="drink-type" x="380" y="346" text-anchor="middle" fill="var(--lime)" stroke="#3c3f18" stroke-width=".8">soft drink</text>
  </svg>

  <!-- Tonic -->
  <svg class="label label--tonic" viewBox="0 0 760 400">
    <use href="#label-shape" fill="var(--tonic-blue)"/>
    <circle cx="326" cy="61" r="7" fill="var(--cream)"/>
    <text class="brand-name" x="390" y="69" text-anchor="middle" fill="var(--ink)">TOLVIK</text>
    <g class="bubble-column" fill="#ffffff">
      <circle cx="380" cy="100" r="4"/><circle cx="378" cy="120" r="5"/><circle cx="382" cy="142" r="4"/>
      <circle cx="379" cy="162" r="6"/><circle cx="383" cy="184" r="4"/><circle cx="380" cy="204" r="5"/>
      <circle cx="376" cy="224" r="3"/>
      <circle cx="250" cy="150" r="6"/><circle cx="290" cy="175" r="4"/><circle cx="270" cy="205" r="7"/>
      <circle cx="310" cy="215" r="4"/><circle cx="225" cy="120" r="3"/>
    </g>
    <text class="drink-name" x="380" y="290" text-anchor="middle" font-size="66" fill="var(--cream)">tonic</text>
    <text class="drink-type" x="380" y="330" text-anchor="middle" fill="#2b8c96">soft drink</text>
  </svg>

  <!-- Cola -->
  <svg class="label label--cola" viewBox="0 0 760 400">
    <use href="#label-shape" fill="var(--cola-red)"/>
    <circle cx="326" cy="61" r="7" fill="var(--cream)"/>
    <text class="brand-name" x="390" y="69" text-anchor="middle" fill="var(--cream)">TOLVIK</text>
    <g role="img" aria-label="Two small stylised cola bottles">
      <rect x="368" y="105" width="24" height="120" rx="10" fill="var(--cola-dark)"/>
    </g>
    <g fill="none" stroke="#f39a7a" stroke-width="2">
      <circle cx="285" cy="140" r="7"/><circle cx="255" cy="170" r="5"/>
      <circle cx="300" cy="210" r="8"/><circle cx="330" cy="180" r="4"/>
    </g>
    <text class="drink-name" x="380" y="292" text-anchor="middle" font-size="72" fill="var(--cream)" stroke="#2a0c14" stroke-width="2">cola</text>
    <text class="drink-type" x="380" y="330" text-anchor="middle" fill="var(--cream)">soft drink</text>
  </svg>

  <!-- Lemon verbena lemonade -->
  <svg class="label label--verbena" viewBox="0 0 760 400">
    <use href="#label-shape" fill="var(--verbena-yellow)"/>
    <circle cx="326" cy="61" r="7" fill="var(--sage)"/>
    <text class="brand-name" x="390" y="69" text-anchor="middle" fill="var(--ink)">TOLVIK</text>
    <g role="img" aria-label="Vertical line of verbena leaves and lemon slices">
      <rect x="362" y="85" width="36" height="140" rx="18" fill="var(--verbena-light)" stroke="#d4c95a" stroke-width="1"/>
    </g>
    <g fill="var(--sage)">
      <circle cx="300" cy="175" r="5"/><circle cx="325" cy="190" r="4"/><circle cx="335" cy="215" r="7"/>
      <circle cx="285" cy="240" r="6"/><circle cx="355" cy="205" r="3"/>
    </g>
    <path d="M285 265 C285 240 330 238 380 240 C440 238 482 245 478 270 C475 300 430 308 380 306 C320 308 283 298 285 265 Z" fill="var(--sage)"/>
    <text class="drink-name" x="380" y="258" text-anchor="middle" font-size="28" fill="#ffffff">lemon</text>
    <text class="drink-name" x="380" y="280" text-anchor="middle" font-size="28" fill="#ffffff">verbena</text>
    <text class="drink-name" x="380" y="302" text-anchor="middle" font-size="28" fill="#ffffff">lemonade</text>
    <text class="drink-type" x="380" y="345" text-anchor="middle" fill="var(--sage-dark)">soft drink</text>
  </svg>

</main>
</body>
</html>
```